Postcard Design Project for construction drywall company

Professional Drywall ContractorSpecializing in Custom Houses We also do additionsWould like a picture of a completed custom houseWould also like a picture of a house under constructionWould also like some pictures of drywall being worked on,I can supply pictures if necessaryI have included a .pdf of our logoWe need a final file in .eps format

Target Market(s)

General Contractors

Industry/Entity Type

Residential Construction

Font styles to use
Sans Serif

Requirements
Must have
• License number picture of houses under construction, picture of completed large phone number bright colors space for label and stamp. Website brookpanel.net
• Custom Houses very large

```html
<!DOCTYPE html>
<html lang="en">
<head>
<meta charset="utf-8">
<title>Brook Panel – Postcard</title>
<link rel="stylesheet" href="https://fonts.googleapis.com/css2?family=Open+Sans:wght@400;700;800&display=swap">
<style>
  :root {
    --bg: #7a7a7a;
    --black: #000000;
    --white: #ffffff;
    --blue: #0a9de0;
    --blue-light: #6cc4ee;
    --stamp: #ebebeb;
    --build-tone: #b7a58c;
    --frame-tone: #a88d74;
    --paint-tone: #d6d6cb;
    --foyer-tone: #c99a7c;
    --room-tone: #9c8a6c;
  }
  * { margin: 0; padding: 0; box-sizing: border-box; }
  html, body { width: 960px; height: 1200px; overflow: hidden; }
  body {
    background: var(--bg);
    font-family: "Open Sans", Arial, sans-serif;
    color: var(--white);
    position: relative;
  }
  .card {
    position: absolute;
    left: 84px;
    width: 806px;
    height: 536px;
    background: var(--white);
    overflow: hidden;
  }
  .card--front { top: 36px; }
  .card--back { top: 626px; }
  .card-art { position: absolute; inset: 0; width: 806px; height: 536px; }
  .text { position: absolute; white-space: nowrap; line-height: 1; }
  .brand-box {
    position: absolute;
    background: var(--black);
    display: flex;
    align-items: center;
    justify-content: center;
    text-align: center;
  }
  .brand-name {
    font-weight: 800;
    color: var(--white);
    line-height: 1.05;
    letter-spacing: 0.5px;
  }
  .headline { font-weight: 800; font-size: 34px; letter-spacing: 1px; }
  .tagline { font-size: 20px; }
  .tagline b { font-weight: 800; }
  .cta { font-size: 24px; }
  .cta b { font-weight: 800; letter-spacing: 0.5px; }
  .phone { font-weight: 800; font-size: 49px; letter-spacing: 1px; }
  .contact { display: flex; align-items: center; gap: 16px; }
  .contact svg { flex: none; }
  .stamp-box { position: absolute; background: var(--stamp); }
</style>
</head>
<body>

<section class="card card--front">
  <svg class="card-art" viewBox="0 0 806 536">
    <rect width="806" height="536" fill="#ffffff"/>
    <polygon points="0,0 292,0 260,194 0,194" fill="var(--build-tone)" role="img" aria-label="Photo of a large house under construction with scaffolding and trucks on the site"/>
    <polygon points="296,0 594,0 562,194 264,194" fill="var(--frame-tone)" role="img" aria-label="Photo of an interior framed with insulation before drywall"/>
    <polygon points="598,0 806,0 806,194 566,194" fill="var(--paint-tone)" role="img" aria-label="Photo of a worker on a ladder finishing drywall in a bright room"/>
    <rect x="0" y="198" width="806" height="139" fill="var(--black)"/>
    <polygon points="0,344 410,344 374,536 0,536" fill="var(--blue)"/>
    <polygon points="414,344 806,344 806,536 378,536" fill="var(--foyer-tone)" role="img" aria-label="Photo of a finished custom home foyer with curved staircase and chandelier"/>
    <line x1="26" y1="444" x2="348" y2="444" stroke="#ffffff" stroke-width="1.5" opacity="0.8"/>
  </svg>

  <div class="brand-box" style="left:362px; top:62px; width:118px; height:134px; border:3px solid #fff;">
    <span class="brand-name" style="font-size:22px;">BROOK<br>PANEL</span>
  </div>

  <div class="text headline" style="left:0; width:806px; text-align:center; top:216px;">DRYWALL AND PAINTING CONTRACTOR</div>
  <div class="text tagline" style="left:0; width:806px; text-align:center; top:263px;">We serve <b>VENTURA, SANTA BARBARA,</b> and <b>LOS ANGELES COUNTIES</b></div>
  <div class="text tagline" style="left:0; width:806px; text-align:center; top:296px;">we are specializing in <b>Custom Houses</b></div>

  <div class="text cta" style="left:25px; top:358px;">Request an <b>ESTIMATE</b></div>
  <div class="text phone" style="left:25px; top:390px;">805-555-0148</div>
  <div class="text contact" style="left:26px; top:454px; font-size:26px;">
    <svg width="18" height="13" viewBox="0 0 18 13"><rect x="0.75" y="0.75" width="16.5" height="11.5" fill="none" stroke="#fff" stroke-width="1.5"/><path d="M1 1 L9 8 L17 1 M1 12 L7 6.5 M17 12 L11 6.5" fill="none" stroke="#fff" stroke-width="1.5"/></svg>
    <span>dale@brookpanel.net</span>
  </div>
  <div class="text contact" style="left:26px; top:491px; font-size:28px;">
    <svg width="16" height="16" viewBox="0 0 16 16"><circle cx="8" cy="8" r="7" fill="none" stroke="#fff" stroke-width="1.4"/><ellipse cx="8" cy="8" rx="3" ry="7" fill="none" stroke="#fff" stroke-width="1.2"/><path d="M1 8 H15 M2.5 4.5 H13.5 M2.5 11.5 H13.5" stroke="#fff" stroke-width="1.2"/></svg>
    <span>www.brookpanel.net</span>
  </div>
</section>

<section class="card card--back">
  <svg class="card-art" viewBox="0 0 806 536">
    <rect width="806" height="536" fill="#ffffff"/>
    <polygon points="0,0 464,0 408,258 0,258" fill="var(--room-tone)" role="img" aria-label="Photo of a finished living room with fireplace, white trim and wood floor"/>
    <polygon points="0,270 404,270 348,536 0,536" fill="var(--black)"/>
    <polygon points="0,381 380,381 368,438 0,438" fill="var(--blue)"/>
    <polygon points="468,0 486,0 368,536 354,536" fill="var(--blue-light)"/>
  </svg>

  <div class="brand-box" style="left:150px; top:232px; width:82px; height:94px; border:2px solid #fff;">
    <span class="brand-name" style="font-size:15px;">BROOK<br>PANEL</span>
  </div>
  <div class="stamp-box" style="left:669px; top:28px; width:109px; height:108px;"></div>

  <div class="text cta" style="left:64px; top:347px;">Request an <b>ESTIMATE</b></div>
  <div class="text phone" style="left:25px; top:383px;">805-555-0148</div>
  <div class="text contact" style="left:34px; top:458px; font-size:24px;">
    <svg width="18" height="13" viewBox="0 0 18 13"><rect x="0.75" y="0.75" width="16.5" height="11.5" fill="none" stroke="#fff" stroke-width="1.5"/><path d="M1 1 L9 8 L17 1 M1 12 L7 6.5 M17 12 L11 6.5" fill="none" stroke="#fff" stroke-width="1.5"/></svg>
    <span>dale@brookpanel.net</span>
  </div>
  <div class="text contact" style="left:34px; top:491px; font-size:26px;">
    <svg width="16" height="16" viewBox="0 0 16 16"><circle cx="8" cy="8" r="7" fill="none" stroke="#fff" stroke-width="1.4"/><ellipse cx="8" cy="8" rx="3" ry="7" fill="none" stroke="#fff" stroke-width="1.2"/><path d="M1 8 H15 M2.5 4.5 H13.5 M2.5 11.5 H13.5" stroke="#fff" stroke-width="1.2"/></svg>
    <span>www.brookpanel.net</span>
  </div>
</section>

</body>
</html>
```